Toward Bright Morrow (TWBM) Business Card - company with a mission

Note* The file attached... orange with "Toward Bright MORROW" (in CAPS) is our logo. I am also open to having the text "toward bright morrow" OUTSIDE the orange round logo for business card (so yes, you may take the text out).

The info: (the following info are separate. So either you can use Martin or Helena for now, but that will be 2 separate cards, not together in one card. Thanks!!

Martin K Pardo
202.555.0183
martin@towardbrightmorrow.example
Managing Partner

Helena R Voss
202.555.0147
helena@towardbrightmorrow.example
Managing Partner

Our website: www.towardbrightmorrow.example

TWBM LLC stands for Toward Bright Morrow (non profit arm is called dawn lift foundation)—our business is based out of New York City and has a non-profit arm where for every bar of soap you purchase, we donate a bar (don’t want any designs that limits us to only soap). Currently working with South Africa. We want the focus to be organic/natural soap with a mission.

Looking for a clean, fresh design.

Industry/Entity Type

Non-Profit

Requirements
Must have
• Clean, fresh, refreshing. Design should not be too busy.

```html
<!DOCTYPE html>
<html lang="en">
<head>
<meta charset="utf-8">
<title>Toward Bright Morrow — Business Card, Helena R Voss</title>
<link rel="stylesheet" href="https://fonts.googleapis.com/css2?family=Encode+Sans+Condensed:wght@200;300;400&display=swap">
<style>
  :root {
    --brand-orange: #f3ae6b;
    --card-white: #ffffff;
    --title-white: rgba(255, 255, 255, 0.78);
    --type: "Encode Sans Condensed", "Arial Narrow", sans-serif;
  }
  * { margin: 0; padding: 0; box-sizing: border-box; }
  html, body {
    width: 1200px;
    height: 975px;
    overflow: hidden;
    background: var(--card-white);
  }
  .card {
    position: relative;
    width: 1200px;
    height: 975px;
    font-family: var(--type);
    background: var(--card-white);
  }
  .brand-side {
    position: absolute;
    left: 0;
    top: 0;
    width: 597px;
    height: 975px;
  }
  .brand-mark {
    position: absolute;
    left: 110px;
    top: 437px;
    width: 336px;
    height: 336px;
  }
  .brand-name {
    position: absolute;
    left: 30px;
    top: 836px;
    width: 520px;
    font-size: 42px;
    font-weight: 300;
    letter-spacing: 0.02em;
    line-height: 1;
    text-transform: uppercase;
    white-space: nowrap;
    color: var(--brand-orange);
  }
  .contact-side {
    position: absolute;
    left: 597px;
    top: 0;
    width: 603px;
    height: 975px;
    overflow: hidden;
    background: var(--brand-orange);
    color: var(--card-white);
  }
  .person-name {
    position: absolute;
    left: 68px;
    top: 20px;
    font-size: 56px;
    font-weight: 400;
    line-height: 1.1;
  }
  .person-title {
    position: absolute;
    left: 68px;
    top: 92px;
    font-size: 38px;
    font-weight: 200;
    line-height: 1.1;
    color: var(--title-white);
  }
  .contact-list {
    position: absolute;
    right: 55px;
    top: 792px;
    width: 510px;
    list-style: none;
    text-align: right;
    font-size: 34px;
    font-weight: 300;
    line-height: 55px;
    white-space: nowrap;
  }
</style>
</head>
<body>
  <main class="card">
    <section class="brand-side">
      <svg class="brand-mark" viewBox="0 0 336 336" aria-hidden="true">
        <circle cx="168" cy="168" r="168" fill="var(--brand-orange)"/>
      </svg>
      <p class="brand-name">Toward Bright Morrow</p>
    </section>
    <section class="contact-side">
      <h1 class="person-name">Helena R Voss</h1>
      <p class="person-title">Managing Partner</p>
      <ul class="contact-list">
        <li class="contact-phone">202.555.0147</li>
        <li class="contact-email">helena@towardbrightmorrow.example</li>
        <li class="contact-web">www.towardbrightmorrow.example</li>
      </ul>
    </section>
  </main>
</body>
</html>
```